Crestline Slate & Tile Needs a Business Card

Attached you will find your logo, my photo and design guidelines for a new business card. The final design will need two separate files to create an embossed card. The cards will be printed by www.plinkprint.com (Instructions below)
Format is the Zib SQUARE card
Crestline Slate And Tile is a brick and mortar, retail stone and tile shop.
One the front:
Crestline Slate And Tile
Gerald Finchcombe
Owner
48207 Vesper Hollow Blvd
Suite R & T
Charlotte, NC 28953
Cell: 704-555-0183
Web: www.CrestlineSlateAndTile.com
(Make each word of the domain a different or alternating color)
On the back;
Something that shows beautiful colorful tile
Follow the design guide closely please. For more information see this page that describes creating the spot gloss file: https://www.plinkprint.com/us/business-cards/design-guidelines-spot-gloss
The logo is what we would like to have raised spot glossed.
Format is the Zib SQUARE card. See attahced guidlines.

```html
<!DOCTYPE html>
<html lang="en">
<head>
<meta charset="utf-8">
<title>Crestline Slate &amp; Tile – Business Card Presentation</title>
<link href="https://fonts.googleapis.com/css2?family=Montserrat:wght@400;500;600;700&display=swap" rel="stylesheet">
<style>
  :root {
    --backdrop: #d8d9d8;
    --card: #ffffff;
    --ink: #111111;
    --slate: #2f3b3d;
    --gold: #b8902f;
    --teal-dark: #3a4a48;
    --brown: #8a5a2e;
    --mark: #444444;
    --tile-blue: #2d3f86;
    --tile-rust: #a5532c;
    --tile-ochre: #d59a3a;
    --tile-cream: #ead8b4;
    --photo-tone: #5b4a42;
  }
  * { box-sizing: border-box; margin: 0; padding: 0; }
  html, body { width: 1200px; height: 1000px; overflow: hidden; }
  body {
    background: var(--backdrop);
    font-family: "Montserrat", sans-serif;
    color: var(--ink);
    position: relative;
  }
  .side-label {
    position: absolute;
    top: 250px;
    font-size: 17px;
    font-weight: 400;
    white-space: nowrap;
    transform: translateX(-50%);
  }
  .side-label strong { font-weight: 700; }
  .side-label--front { left: 381px; }
  .side-label--back { left: 855px; }

  .trim-marks { position: absolute; left: 0; top: 0; }

  .card {
    position: absolute;
    top: 288px;
    height: 464px;
  }
  .card--front {
    left: 136px;
    width: 495px;
    background: var(--card);
  }
  .card--back {
    left: 643px;
    width: 421px;
    background:
      radial-gradient(circle at 30% 30%, var(--tile-ochre) 0 8%, transparent 30%),
      radial-gradient(circle at 75% 65%, var(--tile-rust) 0 10%, transparent 35%),
      linear-gradient(135deg, var(--tile-blue), var(--tile-rust) 45%, var(--tile-blue) 75%, var(--tile-ochre));
  }

  .brand {
    position: absolute;
    left: 47px;
    top: 58px;
    display: flex;
    align-items: center;
    gap: 16px;
  }
  .brand__square {
    width: 60px;
    height: 60px;
    background: var(--slate);
  }
  .brand__name {
    font-size: 22px;
    font-weight: 500;
    letter-spacing: 3px;
    line-height: 1.25;
    color: var(--slate);
    text-transform: uppercase;
  }

  .portrait {
    position: absolute;
    left: 357px;
    top: 46px;
    width: 110px;
    height: 110px;
    border-radius: 50%;
    background: radial-gradient(circle at 50% 40%, #b58c74, var(--photo-tone) 70%);
  }

  .contact {
    position: absolute;
    left: 49px;
    top: 186px;
  }
  .contact__name { font-size: 26px; font-weight: 600; line-height: 32px; }
  .contact__title { font-size: 20px; font-weight: 400; line-height: 26px; margin-bottom: 20px; }
  .contact__address { font-size: 20px; line-height: 30px; margin-bottom: 32px; }
  .contact__phone { font-size: 20px; line-height: 36px; }
  .contact__web { font-size: 20px; line-height: 36px; }
  .web--crest { color: var(--gold); font-weight: 600; }
  .web--slate { color: var(--teal-dark); font-weight: 600; }
  .web--tile { color: var(--brown); font-weight: 600; }
</style>
</head>
<body>
  <p class="side-label side-label--front"><strong>FRONT</strong> (with Raised Spot Gloss on Logo)</p>
  <p class="side-label side-label--back"><strong>BACK</strong> (Colorful Tile Pattern)</p>

  <section class="card card--front">
    <div class="brand">
      <span class="brand__square"></span>
      <span class="brand__name">Crestline<br>Slate &amp; Tile</span>
    </div>
    <div class="portrait" role="img" aria-label="Portrait photo of the owner"></div>
    <div class="contact">
      <h1 class="contact__name">Gerald Finchcombe</h1>
      <p class="contact__title">Owner</p>
      <p class="contact__address">48207 Vesper Hollow Blvd, Suite R &amp; T<br>Charlotte, NC 28953</p>
      <p class="contact__phone">Cell: 704-555-0183</p>
      <p class="contact__web">www.<span class="web--crest">Crestline</span><span class="web--slate">Slate</span><span class="web--tile">AndTile</span>.com</p>
    </div>
  </section>

  <section class="card card--back" role="img" aria-label="Colorful patterned ceramic tile artwork in blue, rust and ochre"></section>

  <svg class="trim-marks" width="1200" height="1000" viewBox="0 0 1200 1000" aria-hidden="true">
    <g stroke="var(--mark)" stroke-width="1">
      <line x1="149" y1="268" x2="149" y2="300"/>
      <line x1="113" y1="300" x2="140" y2="300"/>
      <line x1="617" y1="268" x2="617" y2="300"/>
      <line x1="657" y1="268" x2="657" y2="300"/>
      <line x1="628" y1="300" x2="660" y2="300"/>
      <line x1="1050" y1="268" x2="1050" y2="300"/>
      <line x1="1064" y1="300" x2="1086" y2="300"/>
      <line x1="97" y1="740" x2="140" y2="740"/>
      <line x1="149" y1="752" x2="149" y2="790"/>
      <line x1="617" y1="752" x2="617" y2="790"/>
      <line x1="628" y1="740" x2="660" y2="740"/>
      <line x1="653" y1="752" x2="653" y2="790"/>
      <line x1="1050" y1="752" x2="1050" y2="790"/>
      <line x1="1064" y1="740" x2="1102" y2="740"/>
    </g>
  </svg>
</body>
</html>
```